quorvadeal.com redesign with wireframes, white space and custom form are very important

Need a new two column design that will convert easily to mobile responsive. Lots of white space. Winning design will probably be based on header area and making the custom form stand out. I want the header to be very much like www.talbekmo.com except the form not to go up into the header.
Here are some of the websites I really like:
www.pivrostacks.com
http://glendarokfastmove.com/
http://morquilandestate.com/

We buy homes for cash and close fast. Our target is a home seller who is desperate to sell quickly.
I have uploaded my really ugly wireframe and my logo. I also uploaded my photo for the about us box and a possible photo to use for the header.
The copy on the wireframe is what I will be using except for the about us box.

Here is the exact link for video to frame in the top left box.
https://example-vidhost.net/Kp39xqTzR2a

Number of Pages Required

1 page

Font styles to use
Sans Serif

Colors
0592cd
85cae6
eaf1f7
fbee3d
ec1f27

Requirements
Must have
• Everything on wireframe.
• Must use Verdana font and nothing should be smaller than 12 point. Most should be in 14 point. (except maybe inside of form)

```html
<!DOCTYPE html>
<html lang="en">
<head>
<meta charset="utf-8">
<title>quorvadeal.com — Sell Your Home for Cash</title>
<link href="https://fonts.googleapis.com/css2?family=Questrial&family=Arimo:wght@400;700&display=swap" rel="stylesheet">
<style>
:root{
  --red:#ec3a26;
  --red-dark:#c72e1c;
  --red-band:rgba(214,58,36,.9);
  --field:#f7dcd5;
  --ink:#333;
  --muted:#8a8a8a;
  --rule:#dcdcdc;
  --panel:#f0f0f4;
  --black:#000;
  --white:#fff;
}
*{box-sizing:border-box;margin:0;padding:0}
html,body{width:1200px;height:3172px;overflow:hidden}
body{position:relative;background:var(--white);font-family:"Questrial",sans-serif;color:var(--ink)}
.abs{position:absolute}

/* header */
.brand{left:164px;top:16px;width:193px;height:118px;display:flex;align-items:center;gap:12px}
.brand-mark{width:26px;height:26px;background:var(--red);flex:none}
.brand-name{font-size:30px;color:var(--red);font-weight:400}
.social{right:162px;top:22px;display:flex;gap:14px}
.social span{width:18px;height:18px;border-radius:50%;background:#b9b9b9;display:block}
.phone-top{right:162px;top:58px;font-size:20px;color:var(--red);display:flex;align-items:center;gap:8px}
.nav{left:428px;top:103px;display:flex;gap:42px;font-size:17px;color:#9a9a9a}
.nav a{color:inherit;text-decoration:none}
.nav a.active{color:var(--red)}

/* hero */
.hero{left:0;top:150px;width:1200px;height:370px;background:linear-gradient(180deg,#2c3a52 0%,#3f4c5c 40%,#5d6259 75%,#6a5d45 100%)}
.hero-title{left:0;top:290px;width:1200px;text-align:center;font-family:"Arimo",sans-serif;font-weight:700;font-size:40px;line-height:46px;color:var(--red);-webkit-text-stroke:1.2px var(--white);text-transform:uppercase}

/* form band */
.lead-form{left:0;top:520px;width:1200px;height:149px;background:var(--red-band)}
.lead-form h2{position:absolute;left:172px;top:20px;font-size:21px;font-weight:400;color:var(--white)}
.fields{position:absolute;left:172px;top:64px;display:grid;grid-template-columns:repeat(4,211px);grid-template-rows:34px 32px;gap:10px 4px}
.field{background:var(--field);font-size:13px;color:#555;padding:9px 8px;border:0}
.submit{background:var(--red-dark);color:var(--white);font-size:17px;text-align:center;padding-top:6px;border:0}

/* about */
.avatar{left:566px;top:700px;width:62px;height:62px;border-radius:50%;background:radial-gradient(circle,#a99c8f,#6d7a86)}
.h-section{left:0;width:1200px;text-align:center;color:var(--red);font-weight:400}
.about-title{top:770px;font-size:40px}
.about-text{left:0;top:825px;width:1200px;text-align:center;font-size:17px;line-height:24px;color:var(--muted)}
.divider{left:164px;width:861px;height:1px;background:var(--rule)}
.dots{display:flex;gap:5px;transform:translate(-50%,-50%);left:597px}
.dots i{width:8px;height:8px;border-radius:50%;border:1.5px solid var(--red);display:block}
.dots i.on{background:var(--red)}

.wwd-title{top:956px;font-size:44px}
.wwd-sub{left:0;top:1016px;width:1200px;text-align:center;font-size:16px;color:var(--muted)}
.video{left:161px;top:1076px;width:465px;height:240px;background:#e9e9f3;border:1px solid #d2d2e0;display:flex;align-items:center;justify-content:center}
.ticks{left:682px;top:1128px;list-style:none;font-size:17px;color:var(--muted)}
.ticks li{display:flex;align-items:center;gap:10px;height:44px}

/* sell fast */
.sell-title{left:177px;top:1425px;width:400px;font-size:21px;line-height:26px;color:var(--red)}
.sell-text{left:177px;top:1512px;width:395px;font-size:16px;line-height:23px;color:var(--muted)}
.btn{left:177px;top:1703px;width:167px;height:42px;background:var(--red);color:var(--white);font-size:16px;display:flex;align-items:center;justify-content:center;box-shadow:0 4px 6px rgba(0,0,0,.2)}
.diamond{left:648px;top:1400px;width:296px;height:318px;background:linear-gradient(135deg,#d9c9a3,#4d6f9c 60%,#1f2a44);clip-path:polygon(50% 0,100% 48%,50% 100%,0 48%)}

/* reasons */
.help{left:161px;top:1824px;width:452px;height:238px;background:linear-gradient(180deg,#0f1c3b,#1f3263 60%,#3a3b4c)}
.help-title{position:absolute;left:0;top:100px;width:100%;text-align:center;color:var(--white);font-size:30px}
.help-sub{position:absolute;left:0;top:138px;width:100%;text-align:center;color:#d8d8d8;font-size:14px}
.reasons-title{left:645px;top:1832px;font-size:20px;color:var(--red)}
.reasons{left:645px;top:1870px;list-style:none;font-size:16px;color:var(--muted)}
.reasons li{display:flex;align-items:center;gap:10px;height:33px}

/* testimonials */
.test-title{top:2166px;font-size:40px}
.quote-mark{left:258px;top:2224px;font-size:40px;color:#999;font-family:"Arimo",sans-serif}
.quote{left:280px;top:2252px;width:640px;text-align:center;font-size:17px;line-height:24px;color:var(--muted)}
.quote-by{left:0;top:2322px;width:1200px;text-align:center;font-size:17px;line-height:25px;color:#444}
.arrow{top:2250px}

/* blog */
.blog{left:151px;top:2532px;width:304px;height:243px;background:var(--panel);padding:20px 14px}
.blog h3{font-size:17px;font-weight:400;color:#222;border-bottom:1px solid #bbb;padding-bottom:4px;width:180px}
.blog h3 span{color:var(--red)}
.blog p{font-size:12px;line-height:17px;color:#666;margin-top:14px}
.more{font-size:12px;color:#777;display:flex;align-items:center;gap:6px}
.post-img{top:2532px;width:305px;height:243px}
.caption{width:305px;font-size:14px;line-height:17px;color:var(--red);top:2782px}

/* footer */
.footer{left:0;top:2899px;width:666px;height:273px;background:var(--black);color:var(--white)}
.footer h4{position:absolute;right:22px;top:28px;font-size:21px;font-weight:400}
.contact{position:absolute;left:364px;display:flex;align-items:flex-start;gap:12px;font-size:16px;line-height:22px;width:290px}
.c-icon{width:26px;height:26px;border-radius:50%;background:var(--red);flex:none;display:flex;align-items:center;justify-content:center}
.foot-brand{position:absolute;left:108px;top:112px;font-size:34px;color:#2a1410}
.copyright{position:absolute;left:108px;top:244px;font-size:12px;color:#999}
.map{left:666px;top:2899px;width:534px;height:273px;background:linear-gradient(135deg,#eceae4,#dcdcd2 50%,#e7e4dc)}
</style>
</head>
<body>

<header>
  <div class="abs brand"><span class="brand-mark"></span><span class="brand-name">quorvadeal.com</span></div>
  <div class="abs social"><span></span><span></span><span></span><span></span></div>
  <div class="abs phone-top">
    <svg width="18" height="18" viewBox="0 0 24 24"><path d="M6.6 10.8a15 15 0 0 0 6.6 6.6l2.2-2.2c.3-.3.7-.4 1-.2 1.1.4 2.3.6 3.6.6.6 0 1 .4 1 1V20c0 .6-.4 1-1 1A17 17 0 0 1 3 4c0-.6.4-1 1-1h3.5c.6 0 1 .4 1 1 0 1.3.2 2.5.6 3.6.1.3 0 .7-.2 1z" fill="#ec3a26"/></svg>
    555-014-2290
  </div>
  <nav class="abs nav">
    <a class="active" href="#">Sell Your Home</a>
    <a href="#">How it works</a>
    <a href="#">Stop foreclosure</a>
    <a href="#">Probate</a>
    <a href="#">Contact</a>
  </nav>
</header>

<section>
  <div class="abs hero" role="img" aria-label="Photo of a single-storey house with trees at dusk"></div>
  <h1 class="abs hero-title">Sell your home for cash in 8 days<br>We buy houses nationwide.</h1>
</section>

<form class="abs lead-form">
  <h2>Yes, I want to sell my home fast!</h2>
  <div class="fields">
    <div class="field">Your Name</div>
    <div class="field">Your phone number</div>
    <div class="field">Your Email Address</div>
    <div class="field">Property Address</div>
    <div class="field">Repairs needed if any</div>
    <div class="field">Asking price</div>
    <div class="field">Comments</div>
    <div class="submit">SUBMIT</div>
  </div>
</form>

<section>
  <div class="abs avatar" role="img" aria-label="Portrait photo of the owner"></div>
  <h2 class="abs h-section about-title">ABOUT US</h2>
  <p class="abs about-text">Owned and operated in Orlando Florida since 2001. Oldest Continuous<br>operated website in country.</p>
  <div class="abs divider" style="top:920px"></div>
  <div class="abs dots" style="top:920px"><i class="on"></i></div>
</section>

<section>
  <h2 class="abs h-section wwd-title">WHAT WE DO</h2>
  <p class="abs wwd-sub">These are the benefits of selling your home to us.</p>
  <div class="abs video" aria-label="Video frame: https://example-vidhost.net/Kp39xqTzR2a">
    <svg width="64" height="64" viewBox="0 0 64 64"><circle cx="32" cy="32" r="28" fill="none" stroke="#a0a0a8" stroke-width="6"/><path d="M26 20 L46 32 L26 44Z" fill="#a0a0a8"/></svg>
  </div>
  <ul class="abs ticks">
    <li><svg width="16" height="12" viewBox="0 0 16 12"><path d="M1 6l5 5 9-10" stroke="#9a9a9a" stroke-width="2" fill="none"/></svg>You pick the closing date</li>
    <li><svg width="16" height="12" viewBox="0 0 16 12"><path d="M1 6l5 5 9-10" stroke="#9a9a9a" stroke-width="2" fill="none"/></svg>You pay NO commissions or fees</li>
    <li><svg width="16" height="12" viewBox="0 0 16 12"><path d="M1 6l5 5 9-10" stroke="#9a9a9a" stroke-width="2" fill="none"/></svg>You don't have to paint, clean or make repairs</li>
  </ul>
  <div class="abs divider" style="top:1382px"></div>
  <div class="abs dots" style="top:1382px"><i></i><i class="on"></i></div>
</section>

<section>
  <h3 class="abs sell-title">Sell your home or house fast for cash to aprofessional investor company. We buy Houses and close quickly.</h3>
  <p class="abs sell-text">Selling a home on your own has never been easier. From Orlando to Greensboro - and all points in between- you can sell your home today without any hassles. Call 1-800-555-0147 or fill out the form below to get a written offer on your home in just 36 hours. Sell today online to people that care</p>
  <div class="abs btn">READ MORE</div>
  <div class="abs diamond" role="img" aria-label="Diamond-shaped collage of house photos"></div>
</section>

<section>
  <div class="abs help" role="img" aria-label="Modern house lit up at night">
    <div class="help-title">We Can Help.</div>
    <div class="help-sub">We Are The Fastest House Buyer Around</div>
  </div>
  <h3 class="abs reasons-title">If you need to sell a home fast because of</h3>
  <ul class="abs reasons">
    <li><svg width="14" height="11" viewBox="0 0 16 12"><path d="M1 6l5 5 9-10" stroke="#ec3a26" stroke-width="2" fill="none"/></svg>Divorce or Bankruptcy</li>
    <li><svg width="14" height="11" viewBox="0 0 16 12"><path d="M1 6l5 5 9-10" stroke="#ec3a26" stroke-width="2" fill="none"/></svg>Foreclosure</li>
    <li><svg width="14" height="11" viewBox="0 0 16 12"><path d="M1 6l5 5 9-10" stroke="#ec3a26" stroke-width="2" fill="none"/></svg>Landlord problems - evictions with tenants</li>
    <li><svg width="14" height="11" viewBox="0 0 16 12"><path d="M1 6l5 5 9-10" stroke="#ec3a26" stroke-width="2" fill="none"/></svg>Inherited property in probate</li>
    <li><svg width="14" height="11" viewBox="0 0 16 12"><path d="M1 6l5 5 9-10" stroke="#ec3a26" stroke-width="2" fill="none"/></svg>Termites, mold, flood or fire damage.</li>
    <li><svg width="14" height="11" viewBox="0 0 16 12"><path d="M1 6l5 5 9-10" stroke="#ec3a26" stroke-width="2" fill="none"/></svg>Moving or can't afford mortgage payments</li>
  </ul>
  <div class="abs divider" style="top:2128px"></div>
  <div class="abs dots" style="top:2128px"><i></i><i></i><i class="on"></i></div>
</section>

<section>
  <h2 class="abs h-section test-title">SELLER TESTIMONIALS</h2>
  <svg class="abs arrow" style="left:148px" width="24" height="40" viewBox="0 0 24 40"><path d="M22 2L4 20l18 18" stroke="#ec3a26" stroke-width="4" fill="none"/></svg>
  <svg class="abs arrow" style="left:1026px" width="24" height="40" viewBox="0 0 24 40"><path d="M2 2l18 18L2 38" stroke="#ec3a26" stroke-width="4" fill="none"/></svg>
  <div class="abs quote-mark">&ldquo;</div>
  <p class="abs quote">I just wanted to thank you for buying my home in Cedar Point. You made it fast and easy and kept me well informed the whole way.</p>
  <p class="abs quote-by">Dorin Kessaly<br>Cedar Point</p>
  <div class="abs divider" style="top:2453px"></div>
  <div class="abs dots" style="top:2453px"><i></i><i></i><i></i><i class="on"></i></div>
</section>

<section>
  <div class="abs blog">
    <h3><span>LATEST</span> BLOG</h3>
    <p>Glendarok Fast Move is known for its famous makeovers of old houses, now Glendarok Fast Move has done a different type of makeover – its website! Through its updated website, you now have clearer communication and quicker access ...</p>
    <div class="more" style="margin-top:34px">READ MORE <svg width="12" height="10" viewBox="0 0 12 10"><path d="M0 5h10M6 1l4 4-4 4" stroke="#ec3a26" stroke-width="1.6" fill="none"/></svg></div>
  </div>
  <div class="abs post-img" style="left:457px;background:linear-gradient(180deg,#8fb36e,#b9946a 50%,#7d6a4f)" role="img" aria-label="Photo of a two-storey suburban house"></div>
  <div class="abs post-img" style="left:764px;background:linear-gradient(180deg,#d9dde0,#5b5552 45%,#6f7a5a)" role="img" aria-label="Photo of a dark brick house"></div>
  <p class="abs caption" style="left:457px">Some of the cities where we buy houses. Not all are listed.</p>
  <p class="abs caption" style="left:764px">We buy nice pretty houses and some ugly ones as well.</p>
  <div class="abs more" style="left:669px;top:2833px">READ MORE <svg width="12" height="10" viewBox="0 0 12 10"><path d="M0 5h10M6 1l4 4-4 4" stroke="#ec3a26" stroke-width="1.6" fill="none"/></svg></div>
  <div class="abs more" style="left:980px;top:2833px">READ MORE <svg width="12" height="10" viewBox="0 0 12 10"><path d="M0 5h10M6 1l4 4-4 4" stroke="#ec3a26" stroke-width="1.6" fill="none"/></svg></div>
</section>

<footer>
  <div class="abs footer">
    <h4>CONTACT</h4>
    <div class="foot-brand">quorvadeal.com</div>
    <div class="contact" style="top:76px">
      <span class="c-icon"><svg width="12" height="16" viewBox="0 0 12 16"><path d="M6 0a6 6 0 0 0-6 6c0 4.5 6 10 6 10s6-5.5 6-10a6 6 0 0 0-6-6zm0 8.5A2.5 2.5 0 1 1 6 3.5a2.5 2.5 0 0 1 0 5z" fill="#fff"/></svg></span>
      <span>4410 Marrow Lane #118 Cedar<br>Point, FL 32011</span>
    </div>
    <div class="contact" style="top:144px">
      <span class="c-icon"><svg width="14" height="14" viewBox="0 0 24 24"><path d="M6.6 10.8a15 15 0 0 0 6.6 6.6l2.2-2.2c.3-.3.7-.4 1-.2 1.1.4 2.3.6 3.6.6.6 0 1 .4 1 1V20c0 .6-.4 1-1 1A17 17 0 0 1 3 4c0-.6.4-1 1-1h3.5c.6 0 1 .4 1 1 0 1.3.2 2.5.6 3.6.1.3 0 .7-.2 1z" fill="#fff"/></svg></span>
      <span>555-014-2290</span>
    </div>
    <div class="contact" style="top:192px">
      <span class="c-icon"><svg width="14" height="11" viewBox="0 0 14 11"><rect x=".5" y=".5" width="13" height="10" fill="none" stroke="#fff"/><path d="M.5 .5l6.5 5 6.5-5" stroke="#fff" fill="none"/></svg></span>
      <span>sales@quorvadeal.com</span>
    </div>
    <div class="copyright">©2015 copyright quorvadeal.com</div>
  </div>
  <div class="abs map" role="img" aria-label="Street map showing the office location">
    <svg width="534" height="273" viewBox="0 0 534 273"><path d="M267 105c-14 0-25 11-25 25 0 19 25 44 25 44s25-25 25-44c0-14-11-25-25-25z" fill="#ec3a26"/><circle cx="267" cy="130" r="9" fill="#fff"/><ellipse cx="267" cy="186" rx="26" ry="8" fill="none" stroke="#ec3a26" stroke-width="3"/></svg>
  </div>
</footer>

</body>
</html>
```